**** Business card design for VoltaNode ****

For my ICT company VoltaNode I need I need a business card design.

We design, build and host web-applications and we have our own CMS product.

Some good examples are attached.

The information should be:
Joris Tielenburg
Managing director
E: j.tielenburg@voltanode-example.nl
M: +31(0)6 57218064
T: +31(0)40 7249305
W: www.voltanode-example.nl

Address:
Berend Vlootweg 27
5612 KT Eindhoven

Industry/Entity Type

Business

Requirements
Must have
• - Use logo (see attachments)
- Double sided
- Distinctive
Nice to have
• - Place for a statement on the back-side: "Crafted with insight, delivered with care"
- HTML code (or Wordpress)
- Dark (black or dark-gray) side
- Small simple images for telephone, e-mail en Url.
- QR code (only if not disturbing), not required, just an option

```html
<!DOCTYPE html>
<html lang="en">
<head>
<meta charset="utf-8">
<title>VoltaNode business cards</title>
<link rel="stylesheet" href="https://fonts.googleapis.com/css2?family=Open+Sans:wght@400;600&family=Crimson+Text&display=swap">
<style>
  :root {
    --stage: #d1d4d6;
    --ink-black: #020305;
    --glow-blue: #1b3a5c;
    --navy: #111a2a;
    --paper: #ffffff;
    --cyan: #3fd0e8;
    --title-cyan: #7fd3e6;
    --brand-grey: #7d8d99;
    --tagline-light: #d8dde2;
    --tagline-dark: #4a4f55;
    --text-dark: #1a1a1a;
  }
  * { margin: 0; padding: 0; box-sizing: border-box; }
  html, body { width: 960px; height: 1200px; overflow: hidden; }
  body { background: var(--stage); position: relative; font-family: "Open Sans", sans-serif; }

  .card {
    position: absolute; left: 55px; width: 850px; height: 490px;
    border-radius: 14px; overflow: hidden;
  }
  .card--front {
    top: 90px;
    background: radial-gradient(ellipse 420px 260px at 300px 250px, var(--glow-blue) 0%, #08111c 45%, var(--ink-black) 80%);
  }
  .card--back { top: 616px; background: var(--navy); }
  .card__shape { position: absolute; inset: 0; }

  .brand { position: absolute; display: flex; align-items: center; gap: 18px; }
  .brand__dot { border-radius: 50%; background: var(--cyan); flex: none; }
  .brand__name { font-weight: 400; color: var(--brand-grey); line-height: 1; white-space: nowrap; }

  .front-brand { left: 230px; top: 200px; }
  .front-brand .brand__dot { width: 70px; height: 70px; }
  .front-brand .brand__name { font-size: 60px; }
  .front-tagline {
    position: absolute; left: 318px; top: 280px;
    font-size: 20px; color: var(--tagline-light); white-space: nowrap;
  }

  .person { position: absolute; left: 32px; top: 58px; }
  .person__name { font-size: 31px; color: var(--paper); font-weight: 400; line-height: 1.15; white-space: nowrap; }
  .person__role { font-size: 24px; color: var(--title-cyan); margin-left: 22px; line-height: 1.3; white-space: nowrap; }

  .contacts {
    position: absolute; left: 408px; top: 118px;
    font-family: "Crimson Text", serif; font-size: 20px; color: var(--text-dark);
  }
  .contact { display: flex; gap: 11px; margin-bottom: 12px; line-height: 24px; white-space: nowrap; }
  .contact__icon { width: 22px; height: 22px; flex: none; margin-top: 2px; }
  .address { margin-top: 30px; line-height: 24px; white-space: nowrap; }
  .address__label { color: var(--cyan); }

  .back-brand { left: 74px; top: 382px; gap: 20px; }
  .back-brand .brand__dot { width: 54px; height: 54px; }
  .back-brand .brand__name { font-size: 28px; }
  .back-tagline {
    position: absolute; left: 148px; top: 425px;
    font-size: 17px; color: var(--tagline-dark); white-space: nowrap;
  }
</style>
</head>
<body>

<section class="card card--front" aria-label="Front side">
  <div class="brand front-brand">
    <span class="brand__dot"></span>
    <span class="brand__name">VoltaNode</span>
  </div>
  <p class="front-tagline">"Crafted with insight, delivered with care"</p>
</section>

<section class="card card--back" aria-label="Back side">
  <svg class="card__shape" viewBox="0 0 850 490" aria-hidden="true">
    <path d="M514 0 L850 0 L850 368 C810 420 760 460 710 490 L30 490 C130 300 330 70 514 0 Z" fill="var(--paper)"/>
  </svg>

  <div class="person">
    <h1 class="person__name">Joris Tielenburg</h1>
    <p class="person__role">managing director</p>
  </div>

  <div class="contacts">
    <div class="contact">
      <svg class="contact__icon" viewBox="0 0 22 22" aria-hidden="true">
        <rect x="1" y="5" width="20" height="13" fill="none" stroke="var(--cyan)" stroke-width="1.8"/>
        <path d="M1 5 L11 13 L21 5 M1 18 L8 11 M21 18 L14 11" fill="none" stroke="var(--cyan)" stroke-width="1.6"/>
      </svg>
      <span>j.tielenburg@voltanode-example.nl</span>
    </div>
    <div class="contact">
      <svg class="contact__icon" viewBox="0 0 22 22" aria-hidden="true">
        <rect x="4" y="0" width="14" height="22" rx="2" fill="none" stroke="var(--cyan)" stroke-width="1.8"/>
        <rect x="7" y="3" width="8" height="5" fill="var(--cyan)"/>
        <g fill="var(--cyan)"><rect x="7" y="11" width="2" height="2"/><rect x="10" y="11" width="2" height="2"/><rect x="13" y="11" width="2" height="2"/><rect x="7" y="15" width="2" height="2"/><rect x="10" y="15" width="2" height="2"/><rect x="13" y="15" width="2" height="2"/></g>
      </svg>
      <span>+31(0)6 57218064<br>+31(0)40 7249305</span>
    </div>
    <div class="contact">
      <svg class="contact__icon" viewBox="0 0 22 22" aria-hidden="true">
        <rect x="1" y="2" width="20" height="14" rx="1" fill="none" stroke="var(--cyan)" stroke-width="1.8"/>
        <rect x="4" y="5" width="14" height="8" fill="var(--cyan)"/>
        <rect x="2" y="18" width="18" height="3" fill="var(--cyan)"/>
      </svg>
      <span>www.voltanode-example.nl</span>
    </div>
    <div class="address">
      <p class="address__label">Address:</p>
      <p>Berend Vlootweg 27</p>
      <p>5612 KT Eindhoven</p>
    </div>
  </div>

  <div class="brand back-brand">
    <span class="brand__dot"></span>
    <span class="brand__name">VoltaNode</span>
  </div>
  <p class="back-tagline">"Crafted with insight, delivered with care"</p>
</section>

</body>
</html>
```